new business card design - modern, professional, bold, B2B focus - with QR code pls

we are looking for a modern looking, colorful, business card design. some highlights:
- put space for QR code please. probably on the back but I'm open.
- biz card to be orientated VERTICAL not the traditional horizontal.
- do NOT use our full name on the card (ie: Allied Furnace Servicing Inc). Use only AFS Inc or AFS.
- use black and orange with some white. ideally black card with orange and white for the letters/logo etc. gray ok too - for outlines etc.
- we work in HEAVY industrial, so the cards should lend itself to this. our website is alfurnace.example, so you can see what we do.
- do NOT put in little smoke stack pictures / silouettes etc.
- think MODERN and INDUSTRIAL, with a techy focus.

Industry/Entity Type

heavy industrial - all of them. we perform maintenance and inspection services at heavy industrial and commercial businesses. so B2B

Contact Information for Business Card

name, title, phone numbers (cell + hardline), website, email address. of course our logo too - either on front or front and back.

Font styles to use
Other font styles liked:
• montserrat

Colors
F0912C
F2A743
F7CA91
FBE8D2
FDF5EE

Requirements
Must have
• see description
Nice to have
• see description
Should not have
• see description

```html
<!DOCTYPE html>
<html lang="en">
<head>
<meta charset="utf-8">
<title>AFS Inc – Business Card</title>
<link rel="stylesheet" href="https://fonts.googleapis.com/css2?family=Montserrat:wght@500;600;700;800&display=swap">
<style>
  :root {
    --stage: #e9e6e1;
    --card: #1f2024;
    --card-deep: #1a1b1e;
    --card-deeper: #16171a;
    --emboss: #2c2d32;
    --orange: #f0912c;
    --white: #ffffff;
    --gray: #b9b4ab;
    --qr-field: #f5f2ed;
  }
  * { box-sizing: border-box; margin: 0; padding: 0; }
  html, body { width: 1200px; height: 780px; overflow: hidden; }
  body {
    background: var(--stage);
    font-family: "Montserrat", sans-serif;
    position: relative;
  }
  .card {
    position: absolute;
    top: 60px;
    width: 380px;
    height: 660px;
    border-radius: 26px;
    background: var(--card);
    overflow: hidden;
    box-shadow: 0 14px 30px rgba(0,0,0,.25);
  }
  .card--back { left: 170px; }
  .card--front { left: 650px; }

  /* back */
  .back-mark {
    position: absolute;
    left: 0; right: 0; top: 150px;
    text-align: center;
  }
  .back-mark__name {
    font-size: 150px;
    font-weight: 800;
    color: var(--emboss);
    letter-spacing: -4px;
    line-height: 1;
  }
  .back-mark__domain {
    margin-top: 10px;
    font-size: 18px;
    font-weight: 500;
    color: var(--emboss);
  }
  .qr-space {
    position: absolute;
    left: 50%;
    top: 400px;
    width: 150px;
    height: 150px;
    margin-left: -75px;
    border-radius: 10px;
    background: var(--qr-field);
    border: 4px solid var(--orange);
  }

  /* front */
  .front-bands { position: absolute; inset: 0; }
  .brand {
    position: absolute;
    top: 52px; left: 0; right: 0;
    text-align: center;
  }
  .brand__name {
    font-size: 96px;
    font-weight: 800;
    color: var(--orange);
    letter-spacing: -2px;
    line-height: 1;
  }
  .brand__domain {
    margin-top: 8px;
    font-size: 15px;
    font-weight: 500;
    color: var(--white);
  }
  .person {
    position: absolute;
    top: 228px; left: 0; right: 0;
    text-align: center;
  }
  .person__name {
    font-size: 34px;
    font-weight: 800;
    line-height: 1.1;
  }
  .person__first { color: var(--orange); }
  .person__last { color: var(--white); }
  .person__title {
    font-size: 17px;
    font-weight: 600;
    color: var(--white);
    margin-top: 2px;
  }
  .contact-icons {
    display: flex;
    justify-content: center;
    gap: 8px;
    margin-top: 14px;
  }
  .icon-dot {
    width: 26px; height: 26px;
    border-radius: 50%;
    background: var(--orange);
    display: flex; align-items: center; justify-content: center;
  }
  .icon-dot svg { width: 14px; height: 14px; }
  .contact-list {
    list-style: none;
    margin-top: 12px;
    font-size: 14px;
    font-weight: 600;
    color: var(--white);
    line-height: 1.45;
  }
  .address {
    position: absolute;
    bottom: 62px; left: 0; right: 0;
    text-align: center;
    font-size: 14px;
    font-weight: 600;
    font-style: normal;
    color: var(--white);
    line-height: 1.5;
  }
  .address .icon-dot { margin: 0 auto 12px; }
</style>
</head>
<body>

<section class="card card--back" aria-label="Card back">
  <div class="back-mark">
    <div class="back-mark__name">AFS</div>
    <div class="back-mark__domain">alfurnace.example</div>
  </div>
  <div class="qr-space" role="img" aria-label="Space reserved for QR code"></div>
</section>

<section class="card card--front" aria-label="Card front">
  <svg class="front-bands" viewBox="0 0 380 660" preserveAspectRatio="none" aria-hidden="true">
    <path d="M0 400 Q200 480 380 360 L380 660 L0 660 Z" fill="var(--card-deep)"/>
    <path d="M0 500 Q230 560 380 450 L380 660 L0 660 Z" fill="var(--card-deeper)"/>
  </svg>

  <div class="brand">
    <div class="brand__name">AFS</div>
    <div class="brand__domain">alfurnace.example</div>
  </div>

  <div class="person">
    <h1 class="person__name"><span class="person__first">Tomas</span> <span class="person__last">Kovar</span></h1>
    <p class="person__title">Co-Founder</p>

    <div class="contact-icons">
      <span class="icon-dot"><svg viewBox="0 0 14 14"><rect x="4" y="1.5" width="6" height="11" rx="1.2" fill="none" stroke="#fff" stroke-width="1.4"/></svg></span>
      <span class="icon-dot"><svg viewBox="0 0 14 14"><path d="M3 2 L5.5 2 L6.5 5 L5 6 Q6.5 8.5 8 9 L9 7.5 L12 8.5 L12 11 Q6 12 3 2 Z" fill="#fff"/></svg></span>
      <span class="icon-dot"><svg viewBox="0 0 14 14"><rect x="1.5" y="3" width="11" height="8" rx="1" fill="none" stroke="#fff" stroke-width="1.4"/><path d="M2 3.5 L7 7.5 L12 3.5" fill="none" stroke="#fff" stroke-width="1.4"/></svg></span>
      <span class="icon-dot"><svg viewBox="0 0 14 14"><circle cx="7" cy="7" r="5.3" fill="none" stroke="#fff" stroke-width="1.3"/><ellipse cx="7" cy="7" rx="2.3" ry="5.3" fill="none" stroke="#fff" stroke-width="1.1"/><path d="M1.7 7 H12.3" stroke="#fff" stroke-width="1.1"/></svg></span>
    </div>

    <ul class="contact-list">
      <li>905-555-0142</li>
      <li>877-555-0199</li>
      <li>www.alfurnace.example</li>
      <li>AFSINC@alfurnace.example</li>
    </ul>
  </div>

  <address class="address">
    <span class="icon-dot"><svg viewBox="0 0 14 14"><path d="M7 1.5 A3.8 3.8 0 0 1 10.8 5.3 Q10.8 8 7 12.5 Q3.2 8 3.2 5.3 A3.8 3.8 0 0 1 7 1.5 Z" fill="#fff"/><circle cx="7" cy="5.3" r="1.4" fill="var(--orange)"/></svg></span>
    4120 Mill Creek Road, Unit #2.<br>
    Stanton, On L0B 2K0, Canada.
  </address>
</section>

</body>
</html>
```